Business Card Design Project

Cyber Security. Company name is Orlenta.

Industry/Entity Type

Computer Security

Contact Information for Business Card

Gordon Vastrick
Founder and Chief Hacker

2184 W. Harlow Ave.
Suite 314
Chicago, IL 60689
773.555.0193
gordon.vastrick@orlenta.example
www.orlenta.example

```html
<!DOCTYPE html>
<html lang="en">
<head>
<meta charset="utf-8">
<title>Orlenta Business Card</title>
<link rel="stylesheet" href="https://fonts.googleapis.com/css2?family=Lato:wght@300;400;700&display=swap">
<style>
  :root {
    --backdrop: #50686c;
    --card-dark: #333a48;
    --card-light: #ffffff;
    --brand-blue: #5b73c4;
    --ink: #1d1d1d;
    --ink-soft: #444444;
    --rule: #8a8a8a;
  }
  * { margin: 0; padding: 0; box-sizing: border-box; }
  html, body {
    width: 1200px; height: 1200px; overflow: hidden;
    background: var(--backdrop);
    font-family: 'Lato', Arial, sans-serif;
  }
  .canvas { position: relative; width: 1200px; height: 1200px; }
  .card {
    position: absolute; left: 110px; width: 980px; height: 540px;
    border-radius: 34px; overflow: hidden;
    box-shadow: 0 10px 24px rgba(0,0,0,0.25);
  }
  .card--front { top: 40px; background: var(--card-dark); }
  .card--back { top: 620px; background: var(--card-light); }

  .wordmark {
    position: absolute; display: flex; align-items: center; gap: 16px;
    color: var(--brand-blue); font-weight: 400; letter-spacing: 0.5px;
    white-space: nowrap;
  }
  .wordmark__dot { border-radius: 50%; background: var(--brand-blue); flex: none; }
  .card--front .wordmark { left: 450px; top: 228px; font-size: 62px; }
  .card--front .wordmark__dot { width: 48px; height: 48px; }

  .card--back .wordmark { right: 70px; top: 40px; font-size: 50px; }
  .card--back .wordmark__dot { width: 38px; height: 38px; }

  .rule { position: absolute; height: 2px; background: var(--rule); }
  .rule--top { left: 440px; right: 40px; top: 130px; }
  .rule--mid { left: 60px; right: 40px; top: 245px; }
  .rule--low { left: 60px; right: 300px; top: 430px; }

  .person { position: absolute; left: 60px; top: 150px; }
  .person__name { font-size: 48px; font-weight: 400; color: var(--ink); line-height: 1.05; }
  .person__title { font-size: 24px; font-weight: 400; color: var(--ink-soft); margin-top: 4px; }

  .contact {
    position: absolute; left: 60px; top: 268px;
    display: grid; grid-template-columns: 130px 30px auto; row-gap: 6px;
    font-size: 30px; line-height: 44px;
  }
  .contact__label { color: var(--ink); font-weight: 400; }
  .contact__sep { color: var(--ink-soft); }
  .contact__value { color: var(--ink-soft); font-weight: 300; }

  .address {
    position: absolute; left: 60px; top: 446px;
    font-size: 26px; line-height: 36px; color: var(--ink); font-style: normal;
  }
</style>
</head>
<body>
<main class="canvas">
  <section class="card card--front" aria-label="Card front">
    <div class="wordmark"><span class="wordmark__dot"></span><span>Orlenta</span></div>
  </section>

  <section class="card card--back" aria-label="Card back">
    <div class="wordmark"><span class="wordmark__dot"></span><span>Orlenta</span></div>
    <div class="rule rule--top"></div>
    <div class="person">
      <p class="person__name">Gordon Vastrick</p>
      <p class="person__title">Founder and Chief Hacker</p>
    </div>
    <div class="rule rule--mid"></div>
    <div class="contact">
      <span class="contact__label">Phone</span><span class="contact__sep">:</span><span class="contact__value">773.555.0193</span>
      <span class="contact__label">Email</span><span class="contact__sep">:</span><span class="contact__value">gordon.vastrick@orlenta.example</span>
      <span class="contact__label">Web</span><span class="contact__sep">:</span><span class="contact__value">www.orlenta.example</span>
    </div>
    <div class="rule rule--low"></div>
    <address class="address">
      2184 W. Harlow Ave., Suite 314<br>
      Chicago, IL 60689
    </address>
  </section>
</main>
</body>
</html>
```